Motel Sign - Front

(21/03/12 - I've edited the brief and removing the words "garden view" its not fitting in the designs I'm getting and just want the word motel to be the focus. I have a template/vision of what I want - see the whiteboard sketch of what I'm looking for uploaded today. Definitely open to creatively, new designs and different ideas but the whiteboard design I've done should be a guideline. Keep it fresh/green/white. use the sample photos of green as inspiration. Thanks)
We are a motel set in the mountain country of Victoria - Australia. The front of the motel needs a fresh look. We recently removed a large amount of the garden to expose a brick courtyard fence which the front of the courtyard faces out to the main road. Within the courtyard fence there is a wooden frame and paneling.
We want to have a new sign created to slot into the wooden frame. (see photo) its the white component.
Its a very large and unusual shape and I want to keep it simple but need to fill the in the best way possible.
The space is 940mm high and 4940mm width.
The message of the sign is simple the word "MOTEL". I want people to be able to drive past and glance in and see we are a motel straight away. So the main purpose of the sign is to say "MOTEL".
I am open to colour use to match the space and have impact. I thought a background colour should be 'off white'. I'm open to the colours used to match your design as long as it matches the brief. Maybe a garden green for the emblem.
IN BRIEF:
1) the word "MOTEL"
2) Border/Background that ties in the garden.
The design should be centred, clean and simple, doesn't have to fill the whole space as long as its balanced and centred.
I like cursive and garden like designs for this one - as long its the word MOTEL still has impact. (OPEN TO NEW IDEAS)
I am also open to different ideas and suggestions if you feel you have a better way to take advantage of this space.
The sign will be 7-8 metres from the road itself.
NOTE: the photos show the space and the painted white in the space where the sign will go. The garden in front of this space will be completely cleared.
Motel

```html
<!DOCTYPE html>
<html lang="en">
<head>
<meta charset="utf-8">
<title>Motel Sign – Front</title>
<link rel="stylesheet" href="https://fonts.googleapis.com/css2?family=Open+Sans:wght@800&display=swap">
<style>
  :root {
    --sign-white: #ffffff;
    --frame-line: #111111;
    --leaf-light: #c8dc5a;
    --leaf-mid: #9cc84a;
    --leaf-deep: #4fa43a;
    --outline-green: #0f3a12;
  }
  html, body {
    margin: 0;
    padding: 0;
    width: 1200px;
    height: 526px;
    overflow: hidden;
    background: var(--sign-white);
  }
  .sign-canvas {
    position: relative;
    width: 1200px;
    height: 526px;
  }
  .sign-frame {
    position: absolute;
    left: 21px;
    top: 3px;
    width: 1155px;
    height: 518px;
    border: 2px solid var(--frame-line);
    background: var(--sign-white);
  }
  .sign-art {
    position: absolute;
    left: 0;
    top: 0;
  }
  .motel-word {
    font-family: "Open Sans", Arial, sans-serif;
    font-weight: 800;
    font-size: 216px;
    letter-spacing: 2px;
    fill: var(--sign-white);
    stroke: var(--outline-green);
    stroke-width: 10px;
    stroke-linejoin: round;
    paint-order: stroke fill;
  }
</style>
</head>
<body>
  <div class="sign-canvas">
    <div class="sign-frame"></div>
    <svg class="sign-art" width="1200" height="526" viewBox="0 0 1200 526">
      <defs>
        <linearGradient id="garden-band-fill" x1="0" y1="0" x2="1" y2="1">
          <stop offset="0" stop-color="var(--leaf-mid)"/>
          <stop offset="0.35" stop-color="var(--leaf-light)"/>
          <stop offset="0.7" stop-color="var(--leaf-mid)"/>
          <stop offset="1" stop-color="var(--leaf-deep)"/>
        </linearGradient>
      </defs>
      <rect class="garden-band" x="71" y="160" width="1079" height="207"
            fill="url(#garden-band-fill)" role="img"
            aria-label="Fresh green garden backdrop with white curling vines, ferns and swirls"/>
      <text class="motel-word" x="612" y="340" text-anchor="middle">MOTEL</text>
    </svg>
  </div>
</body>
</html>
```